Business Card Design for sports performance / psychology company

You can see my website that this is based upon here:
http://www.trelvoxcoaching.co.uk

More than happy to answer any additional questions that you might have

** Happy for any images from Pixelgrove to be used. If I go with your design I will purchase the image for you to use

Target Market(s)

Football players

Industry/Entity Type

Business

Contact Information for Business Card

Name: Dewi Ansell
Title: Clinical Hypnotherapist & Strategist
Email address: dewi@trelvoxcoaching.co.uk
Tel: 07481926657

Font styles to use
Other font styles liked:
• Same font as on website. I'm not actually sure what it is

Requirements
Must have
• Tagline:
• Talent x Focus = Achievement
• Build a mind that wins matches
Nice to have
• Happy for designers to be creative
Should not have

```html
<!DOCTYPE html>
<html lang="en">
<head>
<meta charset="utf-8">
<title>Trelvox Coaching – Business Card</title>
<link rel="stylesheet" href="https://fonts.googleapis.com/css2?family=Jost:wght@400&family=Mulish:wght@400;600;700&display=swap">
<style>
  :root {
    --navy: #221c4a;
    --grey-text: #5a5a5f;
    --card: #ffffff;
    --backdrop: #e8e5e1;
    --mark-square: #221c4a;
  }
  * { margin: 0; padding: 0; box-sizing: border-box; }
  html, body { width: 1200px; height: 1000px; overflow: hidden; }
  body {
    position: relative;
    background: var(--backdrop);
    font-family: "Mulish", sans-serif;
    color: var(--navy);
  }
  .card {
    position: absolute;
    left: 266px;
    width: 666px;
    height: 398px;
    background: var(--card);
    overflow: hidden;
  }
  .card--front { top: 74px; }
  .card--back { top: 533px; }

  .brand {
    position: absolute;
    display: flex;
    align-items: center;
    font-family: "Jost", sans-serif;
    font-weight: 400;
    color: var(--navy);
    white-space: nowrap;
  }
  .brand__square { background: var(--mark-square); display: block; flex: none; }
  .card--front .brand { left: 34px; top: 54px; font-size: 29px; gap: 18px; }
  .card--front .brand__square { width: 62px; height: 62px; }
  .card--back .brand { left: 104px; top: 153px; font-size: 35px; gap: 22px; }
  .card--back .brand__square { width: 82px; height: 82px; }

  .person { position: absolute; left: 112px; top: 183px; }
  .person__name { font-size: 19px; letter-spacing: 0.5px; font-weight: 400; }
  .person__name strong { font-weight: 700; }
  .person__title { margin-top: 4px; font-size: 15px; color: var(--grey-text); }

  .contact { position: absolute; left: 112px; top: 262px; list-style: none; }
  .contact__item {
    display: flex; align-items: center; gap: 7px;
    height: 25px; font-size: 15px; color: var(--grey-text);
  }
  .contact__item svg { width: 16px; height: 16px; fill: var(--navy); flex: none; }
  .contact__text strong { font-weight: 600; color: var(--grey-text); }

  .social { position: absolute; left: 463px; top: 312px; display: flex; gap: 10px; }
  .social__dot { width: 16px; height: 16px; border-radius: 50%; background: var(--navy); }

  .rule-thin { position: absolute; left: 0; right: 0; top: 364px; height: 4px; background: var(--navy); }
  .rule-band { position: absolute; left: 0; right: 0; top: 372px; height: 26px; background: var(--navy); }

  .tagline {
    position: absolute; left: 99px; top: 348px;
    font-size: 16px; white-space: nowrap;
  }
  .tagline__main { color: var(--navy); font-weight: 400; }
  .tagline__sep { color: var(--grey-text); margin: 0 8px; }
  .tagline__sub { color: var(--grey-text); }
</style>
</head>
<body>
  <section class="card card--front" aria-label="Business card front">
    <div class="brand"><span class="brand__square"></span>TRELVOX COACHING</div>

    <div class="person">
      <p class="person__name"><strong>DEWI</strong> ANSELL</p>
      <p class="person__title">Clinical Hypnotherapist &amp; Strategist</p>
    </div>

    <ul class="contact">
      <li class="contact__item">
        <svg viewBox="0 0 16 16" aria-hidden="true"><path d="M1 5c0-2 3-3 7-3s7 1 7 3v1h-3V4.5H4V6H1z"/><path d="M4 7h8l2 7H2z"/><circle cx="8" cy="10.5" r="1.8" fill="#fff"/></svg>
        <span class="contact__text">07481926657</span>
      </li>
      <li class="contact__item">
        <svg viewBox="0 0 16 16" aria-hidden="true"><path d="M1 3h14v10H1z"/><path d="M1 3l7 6 7-6" fill="none" stroke="#fff" stroke-width="1.3"/></svg>
        <span class="contact__text">dewi@trelvoxcoaching.co.uk</span>
      </li>
      <li class="contact__item">
        <svg viewBox="0 0 16 16" aria-hidden="true"><circle cx="8" cy="8" r="7"/><path d="M2 8h12M8 1c-3 3-3 11 0 14M8 1c3 3 3 11 0 14" fill="none" stroke="#fff" stroke-width="1"/></svg>
        <span class="contact__text">www.<strong>trelvoxcoaching</strong>.co.uk</span>
      </li>
    </ul>

    <div class="social" aria-label="Social media links">
      <span class="social__dot" role="img" aria-label="Social profile"></span>
      <span class="social__dot" role="img" aria-label="Social profile"></span>
      <span class="social__dot" role="img" aria-label="Social profile"></span>
    </div>

    <div class="rule-thin"></div>
    <div class="rule-band"></div>
  </section>

  <section class="card card--back" aria-label="Business card back">
    <div class="brand"><span class="brand__square"></span>TRELVOX COACHING</div>
    <p class="tagline">
      <span class="tagline__main">Talent x Focus = Achievement</span><span class="tagline__sep">|</span><span class="tagline__sub">Build a mind that wins matches</span>
    </p>
  </section>
</body>
</html>
```